Criação de Papelaria Profissional para Consultoria de Negócios
A empresa queria:
" Consultoria em planejamento estratégico... marketing... aulas.. palestras.. artigos e livros publicados "

```html
<!DOCTYPE html>
<html lang="pt-BR">
<head>
<meta charset="UTF-8">
<title>Pasta Institucional – Ricardo Fontana</title>
<link href="https://fonts.googleapis.com/css2?family=Cinzel:wght@500&family=Montserrat:wght@400;600&display=swap" rel="stylesheet">
<style>
  :root {
    --bg: #e6e4e1;
    --paper: #ffffff;
    --charcoal: #2a2a2a;
    --ink: #1f1f1f;
    --orange: #f0561e;
    --muted: #6b6b6b;
    --faint: rgba(180,180,180,0.22);
  }
  * { margin: 0; padding: 0; box-sizing: border-box; }
  html, body { width: 1200px; height: 1200px; overflow: hidden; background: var(--bg); }
  .folder {
    position: absolute; left: 187px; top: 269px;
    width: 898px; height: 775px;
  }
  .panel { position: absolute; top: 0; height: 775px; }
  .panel--back { left: 0; width: 449px; background: var(--paper); border-top: 6px solid var(--ink); }
  .panel--front { left: 449px; width: 449px; background: var(--charcoal); border-top: 8px solid var(--orange); }
  .decor-disc {
    position: absolute; left: 240px; top: 120px; width: 420px; height: 420px;
    border-radius: 50%; background: var(--faint);
  }
  .brand { position: absolute; text-align: center; font-family: 'Cinzel', serif; font-weight: 500; }
  .brand__dot { display: block; width: 22px; height: 22px; border-radius: 50%; background: var(--orange); margin: 0 auto 14px; }
  .brand--back { left: 0; width: 449px; top: 250px; color: var(--ink); font-size: 24px; letter-spacing: 2px; }
  .brand--front { left: 449px; width: 449px; top: 262px; color: #ffffff; font-size: 30px; letter-spacing: 1px; }
  .brand__tagline {
    display: block; margin-top: 10px; font-family: 'Montserrat', sans-serif; font-weight: 400;
    font-size: 11px; letter-spacing: 8px; color: #ffffff;
  }
  .contact { position: absolute; left: 34px; top: 500px; list-style: none; font-family: 'Montserrat', sans-serif; font-size: 9px; color: var(--muted); }
  .contact li { display: flex; align-items: center; gap: 10px; margin-bottom: 12px; line-height: 1.35; }
  .contact svg { flex: none; }
  .website {
    position: absolute; left: 449px; width: 449px; top: 582px; text-align: center;
    font-family: 'Montserrat', sans-serif; font-weight: 600; font-size: 10px; letter-spacing: 5px; color: #ffffff;
  }
  .pocket { position: absolute; left: 0; top: 555px; }
</style>
</head>
<body>
  <div class="folder">
    <div class="panel panel--back"></div>
    <div class="panel panel--front"></div>
    <div class="decor-disc" aria-hidden="true"></div>

    <div class="brand brand--back"><span class="brand__dot"></span>RF</div>

    <div class="brand brand--front">
      <span class="brand__dot"></span>Ricardo Fontana
      <span class="brand__tagline">O ESTRATEGISTA</span>
    </div>

    <ul class="contact">
      <li>
        <svg width="16" height="16" viewBox="0 0 16 16"><circle cx="8" cy="8" r="8" fill="var(--orange)"/><rect x="4" y="5" width="8" height="6" fill="none" stroke="#fff" stroke-width="1.2"/><path d="M4 5l4 3.5L12 5" fill="none" stroke="#fff" stroke-width="1.2"/></svg>
        <span>contato@ricardofontana.com.br<br>www.ricardofontana.com.br</span>
      </li>
      <li>
        <svg width="16" height="16" viewBox="0 0 16 16"><circle cx="8" cy="8" r="8" fill="var(--orange)"/><path d="M5.5 4.5l2 2-1 1.2a6 6 0 0 0 2 2l1.2-1 2 2-1.2 1.3c-3 0-6.3-3.3-6.3-6.3z" fill="#fff"/></svg>
        <span>(81) 3000-0000<br>(81) 99000-0000</span>
      </li>
      <li>
        <svg width="16" height="16" viewBox="0 0 16 16"><circle cx="8" cy="8" r="8" fill="var(--orange)"/><path d="M8 3.5a3 3 0 0 1 3 3c0 2.2-3 6-3 6s-3-3.8-3-6a3 3 0 0 1 3-3z" fill="#fff"/><circle cx="8" cy="6.5" r="1.1" fill="var(--orange)"/></svg>
        <span>Rua das Palmeiras, 120 - Recife - PE</span>
      </li>
    </ul>

    <div class="website">www.RICARDOFONTANA.com.br</div>

    <svg class="pocket" width="449" height="220" viewBox="0 0 449 220" aria-hidden="true">
      <path d="M0 0 H20 Q40 0 40 20 V60 H449 V135 Q449 220 364 220 H0 Z" fill="var(--orange)"/>
    </svg>
  </div>
</body>
</html>
```